Business Card Design

I need a Business Card that will catch the attention that will not get thrown in a Drawer. I have 23 companies I use for Auto, Home, Life, and Business Insurance. I make sure that people have the best coverage for the $ spent.

Industry/Entity Type

Business

Contact Information for Business Card

Dorlin Insurance Agency, Inc., Marcus Helgren, 4375 West Tamber Lane Quillmont, Lorra 45192 555-281-7496, www.dorlinagency.example, Friendspace, Workline, Circleplus

```html
<!DOCTYPE html>
<html lang="en">
<head>
<meta charset="utf-8">
<title>Dorlin Insurance Agency – Business Card</title>
<link rel="stylesheet" href="https://fonts.googleapis.com/css2?family=Roboto+Condensed:wght@400&family=Tinos:wght@700&display=swap">
<style>
  :root {
    --backdrop: #b3b3b3;
    --card: #4e443c;
    --accent: #f37421;
    --ink: #ffffff;
    --ink-soft: #f1ece8;
  }
  html, body {
    margin: 0;
    padding: 0;
    width: 1200px;
    height: 900px;
    overflow: hidden;
    background: var(--backdrop);
  }
  .card {
    position: absolute;
    left: 100px;
    top: 162px;
    width: 1000px;
    height: 576px;
    background: var(--card);
    box-shadow: 2px 3px 6px rgba(0,0,0,0.35);
    overflow: hidden;
    font-family: "Roboto Condensed", "Arial Narrow", sans-serif;
    color: var(--ink);
  }
  .holder-name {
    position: absolute;
    left: 24px;
    top: 36px;
    margin: 0;
    font-size: 29px;
    font-weight: 400;
    color: var(--ink-soft);
  }
  .stripes {
    position: absolute;
    top: 160px;
    height: 36px;
    background: repeating-linear-gradient(
      to bottom,
      var(--accent) 0px,
      var(--accent) 1px,
      transparent 1px,
      transparent 4px
    );
  }
  .stripes--left { left: 0; width: 240px; }
  .stripes--right { left: 751px; width: 249px; }
  .agency-name {
    position: absolute;
    left: 240px;
    width: 511px;
    top: 154px;
    margin: 0;
    text-align: center;
    font-family: "Tinos", "Times New Roman", serif;
    font-weight: 700;
    font-size: 37px;
    line-height: 46px;
    color: var(--ink);
    white-space: nowrap;
  }
  .contact-band {
    position: absolute;
    left: 0;
    top: 304px;
    width: 604px;
    height: 144px;
    background: var(--accent);
    border-radius: 0 22px 22px 0;
  }
  .contact-list, .social-list {
    list-style: none;
    margin: 0;
    padding: 0;
  }
  .contact-list {
    position: absolute;
    left: 12px;
    top: 10px;
  }
  .contact-list li, .social-list li {
    display: flex;
    align-items: center;
    height: 44px;
    font-size: 27px;
    white-space: nowrap;
  }
  .contact-icon {
    width: 34px;
    height: 34px;
    margin-right: 13px;
    flex: none;
  }
  .social-list {
    position: absolute;
    left: 680px;
    top: 311px;
  }
  .social-icon {
    width: 36px;
    height: 36px;
    margin-right: 18px;
    flex: none;
  }
  .edge-tab {
    position: absolute;
    left: 940px;
    top: 303px;
    width: 60px;
    height: 144px;
    background: var(--accent);
    border-radius: 22px 0 0 22px;
  }
</style>
</head>
<body>
  <main class="card">
    <h2 class="holder-name">Marcus Helgren</h2>

    <div class="stripes stripes--left"></div>
    <h1 class="agency-name">Dorlin Insurance Agency, Inc.</h1>
    <div class="stripes stripes--right"></div>

    <section class="contact-band">
      <ul class="contact-list">
        <li>
          <svg class="contact-icon" viewBox="0 0 34 34" aria-hidden="true">
            <circle cx="17" cy="17" r="16" fill="#fff"/>
            <path d="M8 14 q9 -7 18 0 l-2 3 h-3 v-3 h-8 v3 h-3 z" fill="#f37421"/>
            <rect x="10" y="17" width="14" height="8" rx="2" fill="#f37421"/>
            <circle cx="17" cy="21" r="2" fill="#fff"/>
          </svg>
          <span>555-281-7496</span>
        </li>
        <li>
          <svg class="contact-icon" viewBox="0 0 34 34" aria-hidden="true">
            <circle cx="17" cy="17" r="16" fill="#fff"/>
            <g fill="none" stroke="#f37421" stroke-width="1.6">
              <circle cx="17" cy="17" r="10"/>
              <ellipse cx="17" cy="17" rx="4.5" ry="10"/>
              <line x1="7" y1="17" x2="27" y2="17"/>
              <line x1="9" y1="12" x2="25" y2="12"/>
              <line x1="9" y1="22" x2="25" y2="22"/>
            </g>
          </svg>
          <span>www.dorlinagency.example</span>
        </li>
        <li>
          <svg class="contact-icon" viewBox="0 0 34 34" aria-hidden="true">
            <circle cx="17" cy="17" r="16" fill="#fff"/>
            <path d="M17 28 C11 20 10 17 10 14 a7 7 0 0 1 14 0 c0 3 -1 6 -7 14 z" fill="#f37421"/>
            <circle cx="17" cy="14" r="3" fill="#fff"/>
          </svg>
          <span>4375 West Tamber Lane Quillmont, Lorra 45192</span>
        </li>
      </ul>
    </section>

    <ul class="social-list">
      <li>
        <svg class="social-icon" viewBox="0 0 36 36" aria-hidden="true">
          <circle cx="18" cy="18" r="16" fill="#fff" stroke="#f37421" stroke-width="3"/>
        </svg>
        <span>Friendspace</span>
      </li>
      <li>
        <svg class="social-icon" viewBox="0 0 36 36" aria-hidden="true">
          <circle cx="18" cy="18" r="16" fill="#fff" stroke="#f37421" stroke-width="3"/>
        </svg>
        <span>Circleplus</span>
      </li>
      <li>
        <svg class="social-icon" viewBox="0 0 36 36" aria-hidden="true">
          <circle cx="18" cy="18" r="16" fill="#fff" stroke="#f37421" stroke-width="3"/>
        </svg>
        <span>Workline</span>
      </li>
    </ul>

    <div class="edge-tab"></div>
  </main>
</body>
</html>
```